Business Card Design Project

QPR Management Consulting, LLC is a management consulting firm focused on improving an organization’s health and wellness while enhancing company performance with an emphasis on winning in the marketplace, profitable growth, team building, culture enablement and innovation.

Industry/Entity Type

Business

```html
<!DOCTYPE html>
<html lang="en">
<head>
<meta charset="utf-8">
<title>QPR Management Consulting – Business Cards</title>
<link href="https://fonts.googleapis.com/css2?family=Open+Sans:wght@400;700&display=swap" rel="stylesheet">
<style>
  :root {
    --stage: #0e0e0e;
    --card: #222221;
    --card-shadow: rgba(0,0,0,0.6);
    --accent: #86c043;
    --accent-soft: #9ccd5e;
    --ink-light: #ffffff;
  }
  * { margin: 0; padding: 0; box-sizing: border-box; }
  html, body {
    width: 1200px; height: 1000px; overflow: hidden;
    background: var(--stage);
    font-family: "Open Sans", Arial, sans-serif;
  }
  .stage { position: relative; width: 1200px; height: 1000px; }
  .card {
    position: absolute;
    width: 500px; height: 286px;
    background: var(--card);
    border-radius: 18px;
    overflow: hidden;
    box-shadow: 0 10px 24px var(--card-shadow);
  }
  .card--back { left: 70px; top: 250px; }
  .card--front { left: 630px; top: 470px; }

  .company-name {
    position: absolute;
    color: var(--ink-light);
    font-weight: 400;
    font-size: 17px;
    line-height: 1.25;
    letter-spacing: 0.2px;
  }
  .card--back .company-name { left: 0; right: 0; top: 130px; text-align: center; }
  .card--front .company-name { left: 34px; top: 60px; width: 200px; }

  .card-band {
    position: absolute;
    left: 0; right: 0; bottom: 0;
    height: 92px;
    background: linear-gradient(180deg, var(--accent-soft), var(--accent));
  }

  .contact {
    position: absolute;
    left: 300px; top: 56px;
    color: var(--ink-light);
  }
  .contact__name { color: var(--accent); font-weight: 700; font-size: 17px; line-height: 1.2; }
  .contact__role { font-size: 12px; margin-bottom: 12px; }
  .contact__list { list-style: none; font-size: 13px; }
  .contact__item { display: flex; align-items: center; gap: 8px; line-height: 20px; }
  .contact__icon { width: 12px; height: 12px; flex: none; }
</style>
</head>
<body>
<main class="stage">

  <section class="card card--back" aria-label="Business card back">
    <p class="company-name">QPR Management Consulting, LLC</p>
  </section>

  <section class="card card--front" aria-label="Business card front">
    <div class="card-band" role="img" aria-label="Decorative green band along the lower edge of the card"></div>

    <p class="company-name">QPR Management Consulting, LLC</p>

    <div class="contact">
      <p class="contact__name">John Doe</p>
      <p class="contact__role">Manager</p>
      <ul class="contact__list">
        <li class="contact__item">
          <svg class="contact__icon" viewBox="0 0 12 12" aria-hidden="true"><rect x="3" y="0.5" width="6" height="11" rx="1" fill="none" stroke="var(--accent)" stroke-width="1.2"/><circle cx="6" cy="9.6" r="0.7" fill="var(--accent)"/></svg>
          <span>123.456.7890</span>
        </li>
        <li class="contact__item">
          <svg class="contact__icon" viewBox="0 0 12 12" aria-hidden="true"><rect x="0.5" y="2" width="11" height="8" fill="var(--accent)"/><path d="M0.5,2 L6,6.5 L11.5,2" fill="none" stroke="var(--card)" stroke-width="1"/></svg>
          <span>john@youremail.com</span>
        </li>
        <li class="contact__item">
          <svg class="contact__icon" viewBox="0 0 12 12" aria-hidden="true"><circle cx="6" cy="6" r="5.3" fill="var(--accent)"/><path d="M0.7,6 H11.3 M6,0.7 V11.3 M6,0.7 C3,3 3,9 6,11.3 M6,0.7 C9,3 9,9 6,11.3" fill="none" stroke="var(--card)" stroke-width="0.8"/></svg>
          <span>www.websitename.com</span>
        </li>
      </ul>
    </div>
  </section>

</main>
</body>
</html>
```